R7 Web Design Project

New company website for Intel cyber security company.

Style should be cool, but remain appropriate for very serious subject matter and audience.

Target Market(s)

Target audience is government and the military

Navigation needs to include:
- About Us
- Services
- Careers
- Contact Us
- Contracts

As well as 2 feature areas - use "Technology Integration" and "Case Study" as the supporting headlines.

Industry/Entity Type

Security

Font styles to use
Sans Serif

Colors

Designer to choose colors to be used in the design.

Requirements
Must have
• Mountain imagery and theme.

Use logo attached.

New Tagline - "Securing the Continuum"
Nice to have
• Supporting imagery could include photos representative of security - avoid cliches.
Should not have
• Needs to be serious not frivolous

```html
<!DOCTYPE html>
<html lang="en">
<head>
<meta charset="utf-8">
<title>R7 Group — Securing the Continuum</title>
<link rel="stylesheet" href="https://fonts.googleapis.com/css2?family=Montserrat:wght@400;500&family=Lato:wght@300;400;700&display=swap">
<style>
  :root {
    --navy: #000f5f;
    --brand-blue: #457cbf;
    --deep-blue: #1a3a8c;
    --title-blue: #34549e;
    --charcoal: #2a2a2a;
    --ink: #3a3a3a;
    --muted: #9a9a9a;
    --white: #ffffff;
    --band-top: #f4f4f4;
    --band-bottom: #e4e4e4;
    --ring: #a9a9a9;
  }
  * { box-sizing: border-box; margin: 0; padding: 0; }
  html, body { width: 1200px; height: 823px; overflow: hidden; }
  body {
    position: relative;
    background: var(--band-top);
    font-family: "Lato", sans-serif;
    color: var(--ink);
  }

  /* Header */
  .site-header {
    position: absolute; left: 0; top: 0; width: 1200px; height: 67px;
    background: var(--white);
    box-shadow: 0 2px 4px rgba(0,0,0,0.25);
    z-index: 3;
  }
  .brand {
    position: absolute; left: 131px; top: 8px; height: 51px;
    display: flex; align-items: center; gap: 12px;
    text-decoration: none;
  }
  .brand-mark { width: 51px; height: 51px; background: var(--navy); }
  .brand-name {
    font-family: "Lato", sans-serif; font-weight: 400;
    font-size: 29px; color: var(--navy); letter-spacing: 0.5px;
  }
  .main-nav {
    position: absolute; right: 112px; top: 22px;
    display: flex; list-style: none;
  }
  .main-nav li {
    font-family: "Montserrat", sans-serif; font-size: 14px; color: #444;
    padding: 2px 18px; border-left: 1px solid #e2e2e2;
  }
  .main-nav li:first-child { border-left: none; }
  .main-nav li:last-child { padding-right: 0; }

  /* Hero */
  .hero {
    position: absolute; left: 0; top: 67px; width: 1200px; height: 474px;
    background:
      linear-gradient(180deg, rgba(0,0,0,0) 55%, rgba(40,50,90,0.35) 100%),
      linear-gradient(180deg, #6b8c9c 0%, #8fa9b3 30%, #a7b6b8 48%, #6e7b86 64%, #c8b7a3 76%, #4d5c7a 88%, #2f3d66 100%);
  }
  .hero-title {
    position: absolute; left: 0; top: 98px; width: 1200px; text-align: center;
    font-family: "Montserrat", sans-serif; font-weight: 400;
    font-size: 44px; color: var(--white); letter-spacing: 0.3px;
  }
  .hero-lede {
    position: absolute; left: 300px; top: 163px; width: 600px; text-align: center;
    font-size: 22px; line-height: 28px; color: var(--white);
  }

  /* Services band */
  .services-band {
    position: absolute; left: 0; top: 541px; width: 1200px; height: 211px;
    background: linear-gradient(180deg, var(--band-top), var(--band-bottom));
  }
  .service {
    position: absolute; top: 482px; width: 242px; height: 250px;
    padding: 113px 0 0 15px;
    z-index: 2;
  }
  .service.is-featured {
    background: linear-gradient(160deg, #5d8fd3 0%, #3f6fb9 35%, #1b3d92 75%, #10308a 100%);
    box-shadow: 0 2px 6px rgba(0,0,0,0.25);
    border-radius: 2px;
  }
  .service-icon {
    position: absolute; left: 72px; top: 11px; width: 98px; height: 98px;
    border-radius: 50%; background: var(--ring);
    display: flex; align-items: center; justify-content: center;
  }
  .is-featured .service-icon { background: rgba(255,255,255,0.25); }
  .service-icon-core {
    width: 82px; height: 82px; border-radius: 50%;
    background: linear-gradient(180deg, #4a7fc4, #2f5ea8);
    display: flex; align-items: center; justify-content: center;
  }
  .is-featured .service-icon-core { background: linear-gradient(180deg, #ffffff, #dcdcdc); }
  .service-title {
    font-weight: 300; font-size: 22px; line-height: 25px; color: var(--title-blue);
    margin-bottom: 5px;
  }
  .is-featured .service-title { color: var(--white); }
  .service-list { list-style: none; font-size: 13px; line-height: 16.5px; }
  .service-list li { position: relative; padding-left: 17px; }
  .service-list li::before {
    content: ""; position: absolute; left: 3px; top: 6px;
    width: 5px; height: 5px; border-radius: 50%; background: currentColor;
  }
  .is-featured .service-list { color: var(--white); font-weight: 700; }
  .service-list.is-tight li { margin-bottom: 1px; }

  /* Footer */
  .site-footer {
    position: absolute; left: 0; top: 752px; width: 1200px; height: 71px;
    background: var(--charcoal);
  }
  .footer-links {
    position: absolute; left: 131px; top: 26px;
    font-size: 15px; color: var(--muted); word-spacing: 2px;
  }
  .footer-links .sep { margin: 0 8px; }
  .footer-brand {
    position: absolute; right: 130px; top: 16px; height: 38px;
    display: flex; align-items: center; gap: 10px;
  }
  .footer-brand .brand-mark { width: 38px; height: 38px; background: #6a6a6a; }
  .footer-brand .brand-name { font-size: 24px; color: #8c8c8c; }
</style>
</head>
<body>
  <header class="site-header">
    <a class="brand" href="#">
      <span class="brand-mark"></span>
      <span class="brand-name">R7 GROUP</span>
    </a>
    <ul class="main-nav">
      <li>About Us</li>
      <li>Services</li>
      <li>Careers</li>
      <li>Contact Us</li>
      <li>Contracts</li>
    </ul>
  </header>

  <section class="hero" role="img" aria-label="Snow-capped mountain range under a cool blue sky with clouds in the valley">
    <h1 class="hero-title">Securing the Continuum</h1>
    <p class="hero-lede">Lorem Ipsum is simply dummy text of the printing and typesetting industry.</p>
  </section>

  <div class="services-band"></div>

  <article class="service is-featured" style="left:121px">
    <div class="service-icon"><div class="service-icon-core">
      <svg width="50" height="40" viewBox="0 0 50 40" aria-hidden="true">
        <path d="M2 6h14l4 4h24v4H10L4 36H2z" fill="#000f5f"/>
        <path d="M10 14h38l-6 22H4z" fill="#000f5f"/>
        <rect x="24" y="21" width="12" height="10" rx="1" fill="#fff"/>
        <path d="M26 21v-3a4 4 0 0 1 8 0v3" fill="none" stroke="#fff" stroke-width="2"/>
        <circle cx="30" cy="26" r="1.6" fill="#000f5f"/>
      </svg>
    </div></div>
    <h2 class="service-title">Application<br>Profession Services</h2>
    <ul class="service-list">
      <li>Legacy Modernization</li>
      <li>Development</li>
      <li>Re-engineering / Migration</li>
    </ul>
  </article>

  <article class="service" style="left:363px; padding-left:20px">
    <div class="service-icon"><div class="service-icon-core">
      <svg width="44" height="44" viewBox="0 0 44 44" aria-hidden="true">
        <circle cx="22" cy="22" r="20" fill="#fff"/>
        <circle cx="22" cy="19" r="5" fill="#2f5ea8"/>
        <path d="M20 22h4l1 10h-6z" fill="#2f5ea8"/>
        <path d="M9 21l3-2v4zM35 21l-3-2v4z" fill="#2f5ea8"/>
      </svg>
    </div></div>
    <h2 class="service-title">IT Consultancy<br>Services</h2>
    <ul class="service-list">
      <li>Global Consultation</li>
      <li>IT Resources Analysis</li>
      <li>Employee Portals</li>
    </ul>
  </article>

  <article class="service" style="left:605px; padding-left:15px">
    <div class="service-icon"><div class="service-icon-core">
      <svg width="46" height="46" viewBox="0 0 46 46" aria-hidden="true">
        <g fill="#fff">
          <circle cx="18" cy="18" r="10"/>
          <g stroke="#fff" stroke-width="5">
            <path d="M18 3v30M3 18h30M7 7l22 22M29 7L7 29"/>
          </g>
          <circle cx="34" cy="34" r="5"/>
          <g stroke="#fff" stroke-width="3">
            <path d="M34 26v16M26 34h16M28.5 28.5l11 11M39.5 28.5l-11 11"/>
          </g>
        </g>
        <circle cx="18" cy="18" r="4" fill="#3a6ab3"/>
        <circle cx="34" cy="34" r="2" fill="#3a6ab3"/>
      </svg>
    </div></div>
    <h2 class="service-title">Independent Testing</h2>
    <ul class="service-list is-tight">
      <li>Business Requirements Analysis</li>
      <li>System Integration Testing (SIT)</li>
      <li>Performance Testing</li>
    </ul>
  </article>

  <article class="service" style="left:847px; padding-left:15px; width:260px">
    <div class="service-icon"><div class="service-icon-core">
      <svg width="48" height="34" viewBox="0 0 48 34" aria-hidden="true">
        <rect x="7" y="2" width="34" height="24" rx="2" fill="none" stroke="#fff" stroke-width="3"/>
        <path d="M1 28h46l-3 4H4z" fill="#fff"/>
      </svg>
    </div></div>
    <h2 class="service-title">Application Security</h2>
    <ul class="service-list is-tight">
      <li>Identity &amp;Access Management and Web SSO</li>
      <li>Enterprise SSO - Single Sign On solution for integrated windows...</li>
    </ul>
  </article>

  <footer class="site-footer">
    <p class="footer-links">© R7 Group<span class="sep">/</span>Terms<span class="sep">/</span>Privacy</p>
    <div class="footer-brand">
      <span class="brand-mark"></span>
      <span class="brand-name">R7 GROUP</span>
    </div>
  </footer>
</body>
</html>
```